New Brochure Design Project - downloadable PDF

Capability Statement, Brochure and Website - we are looking for a uniform of the three marketing assets that deliver a professional look and feel for executive-level decision-makers. Our company provides guest and patient-facing technologies. For the most part, the technologies are: smart TVs, Wi-Fi, RTLS, Integrated services. I have submitted the editable files we have, but in terms of industry images, we are happy to have others recommended. I have also submitted previous efforts and one Capability Statement from a company (QDN) that is well received.
Updates
Need extra days to review
Target Market(s)
Corporate and Government Procurement (Healthtcare and Hotels/Resorts)
Industry/Entity Type
Healthcare and Hotel/Resorts
Look and feel

```html
<!DOCTYPE html>
<html lang="en">
<head>
<meta charset="utf-8">
<title>Meridel Brochure</title>
<link rel="stylesheet" href="https://fonts.googleapis.com/css2?family=Montserrat:wght@500;600;700&family=Tinos:wght@400;700&display=swap">
<style>
  :root {
    --bg: #d9d9d9;
    --paper: #ffffff;
    --navy: #2a63a8;
    --teal: #26b8c6;
    --ink: #1c2530;
    --logo-ink: #0f2a3a;
    --rule: #4a78b8;
    --serif: "Tinos", "Times New Roman", serif;
    --sans: "Montserrat", Arial, sans-serif;
  }
  * { box-sizing: border-box; margin: 0; padding: 0; }
  html, body { width: 667px; height: 1200px; overflow: hidden; }
  body { background: var(--bg); position: relative; font-family: var(--sans); }

  .page {
    position: absolute; width: 300px; height: 420px;
    background: var(--paper); overflow: hidden;
    box-shadow: 0 3px 10px rgba(0,0,0,.18);
  }
  .page--cover { left: 183px; top: 145px; }
  .page--features { left: 20px; top: 610px; }
  .page--intro { left: 347px; top: 610px; }

  .page-frame {
    position: absolute; left: 9px; right: 9px; top: 9px; bottom: 20px;
    border: 1px solid var(--rule); border-bottom: none;
  }

  .page-footer { position: absolute; left: 0; bottom: 0; width: 300px; height: 36px; }
  .page-footer svg { position: absolute; inset: 0; }
  .footer-url {
    position: absolute; left: 27px; bottom: 9px;
    color: #fff; font-size: 8.6px; font-weight: 600; letter-spacing: .4px;
  }
  .footer-brand {
    position: absolute; right: 14px; bottom: 10px;
    display: flex; align-items: center; gap: 4px;
    font-family: var(--sans); font-weight: 700; font-size: 10.5px; color: var(--logo-ink);
  }
  .footer-brand--light { color: #fff; font-size: 12px; bottom: 11px; right: 18px; }
  .brand-dot { width: 6px; height: 6px; background: currentColor; }

  .cover-brand {
    position: absolute; top: 18px; left: 0; right: 0; text-align: center;
    font-family: var(--serif); font-weight: 700; font-size: 30px; color: var(--navy);
    text-transform: uppercase; letter-spacing: 1px;
  }
  .cover-photo-backing {
    position: absolute; left: 22px; top: 80px; width: 262px; height: 232px;
    background: var(--navy); transform: rotate(-4deg);
  }
  .cover-photo {
    position: absolute; left: 27px; top: 87px; width: 246px; height: 221px;
    background: linear-gradient(135deg, #e6e4e0 0%, #b99b7e 40%, #3fb3a8 62%, #eef0f2 100%);
  }
  .headline {
    position: absolute; font-family: var(--serif); font-weight: 700;
    line-height: 1.06; text-transform: uppercase;
  }
  .headline .line-teal { color: var(--teal); display: block; }
  .headline .line-navy { color: var(--navy); display: block; }
  .page--cover .headline { left: 15px; top: 330px; font-size: 21px; }

  .features-title { left: 25px; top: 16px; font-size: 18.5px; }
  .feature {
    position: absolute; width: 96px; margin-left: -48px; text-align: center;
    font-family: var(--serif); font-size: 7.8px; line-height: 1.15; color: var(--ink);
    text-transform: uppercase;
  }
  .feature .hl { color: var(--teal); }
  .feature-icon {
    display: block; width: 42px; height: 42px; margin: 0 auto 4px;
    border-radius: 50%; border: 1px solid var(--navy); padding: 2px;
  }
  .feature-icon span {
    display: flex; width: 100%; height: 100%; border-radius: 50%;
    background: radial-gradient(circle at 35% 30%, #2aa6c8, var(--navy) 85%);
    align-items: center; justify-content: center;
  }
  .feature-icon svg { width: 20px; height: 20px; fill: none; stroke: #fff; stroke-width: 1.4; stroke-linecap: round; stroke-linejoin: round; }

  .intro-photo {
    position: absolute; left: 0; top: 0; width: 300px; height: 249px;
    background: linear-gradient(160deg, #f4f6f8 0%, #dde3ea 45%, #c8d2dc 70%, #f2f4f6 100%);
  }
  .page--intro .headline { left: 25px; top: 264px; font-size: 17.5px; }
  .intro-body {
    position: absolute; left: 25px; top: 315px; width: 256px;
    font-size: 5.5px; line-height: 1.45; color: var(--ink); font-weight: 500;
  }
  .intro-body b { font-weight: 700; }
  .intro-lead { position: absolute; left: 25px; top: 344px; font-size: 5.5px; color: var(--ink); font-weight: 500; }
  .intro-lead b { font-weight: 700; }
  .intro-tagline {
    position: absolute; left: 25px; top: 353px;
    font-family: var(--serif); font-weight: 700; font-size: 12.5px; color: var(--navy);
  }
</style>
</head>
<body>

<section class="page page--cover">
  <div class="cover-brand">Meridel</div>
  <div class="cover-photo-backing"></div>
  <div class="cover-photo" role="img" aria-label="Photo of a nurse in teal scrubs holding a tablet beside a smiling senior patient in a hospital bed"></div>
  <h1 class="headline">
    <span class="line-teal">Smart Patient</span>
    <span class="line-navy">Engagement Solution</span>
  </h1>
  <footer class="page-footer">
    <svg width="300" height="36" viewBox="0 0 300 36">
      <rect x="0" y="9" width="300" height="27" fill="var(--navy)"/>
      <polygon points="159,36 175,0 300,0 300,36" fill="var(--teal)"/>
    </svg>
    <span class="footer-url">www.wardlight.com</span>
    <span class="footer-brand"><i class="brand-dot"></i>Wardlight</span>
  </footer>
</section>

<section class="page page--features">
  <div class="page-frame"></div>
  <h2 class="headline features-title">
    <span class="line-teal">Features of the</span>
    <span class="line-navy">NVQ Point-of-Care</span>
  </h2>

  <div class="feature" style="left:56px; top:70px;">
    <i class="feature-icon"><span><svg viewBox="0 0 24 24"><rect x="3" y="7" width="18" height="12" rx="2"/><path d="M9 3l3 4 3-4"/></svg></span></i>
    <span class="hl">Free-to-air</span><br>Television
  </div>
  <div class="feature" style="left:153px; top:70px;">
    <i class="feature-icon"><span><svg viewBox="0 0 24 24"><rect x="4" y="9" width="16" height="11" rx="1"/><path d="M4 9l15-4 1 3"/><path d="M11 12v5l4-2.5z"/></svg></span></i>
    <span class="hl">VOD</span> Movies
  </div>
  <div class="feature" style="left:248px; top:70px;">
    <i class="feature-icon"><span><svg viewBox="0 0 24 24"><circle cx="12" cy="12" r="9"/><path d="M9 6v12M7.5 6v3.5a1.5 1.5 0 003 0V6M15 18V6c1.8 1 2 4 0 6"/></svg></span></i>
    <span class="hl">Food</span><br>Ordering
  </div>

  <div class="feature" style="left:104px; top:143px;">
    <i class="feature-icon"><span><svg viewBox="0 0 24 24"><rect x="4" y="4" width="16" height="16" rx="1"/><path d="M7 8h10M7 12h6M7 16h6M15 12l1 1 2-2M15 16l1 1 2-2"/></svg></span></i>
    <span class="hl">Create your<br>own</span> surveys<br>&amp; quizzes
  </div>
  <div class="feature" style="left:202px; top:143px;">
    <i class="feature-icon"><span><svg viewBox="0 0 24 24"><circle cx="12" cy="12" r="9"/><path d="M10 6h4v4h4v4h-4v4h-4v-4H6v-4h4z"/></svg></span></i>
    <span class="hl">Hospital</span><br>Information
  </div>

  <div class="feature" style="left:56px; top:228px;">
    <i class="feature-icon"><span><svg viewBox="0 0 24 24"><path d="M3 5h10v7H8l-3 3v-3H3zM11 12h10v7h-2v3l-3-3h-5z"/><path d="M6 8h4M15 17l1.5-4 1.5 4"/></svg></span></i>
    <span class="hl">Multilingual</span>
  </div>
  <div class="feature" style="left:153px; top:228px;">
    <i class="feature-icon"><span><svg viewBox="0 0 24 24"><rect x="3" y="4" width="18" height="16" rx="1"/><path d="M3 8h18"/><circle cx="12" cy="14" r="2.5"/><path d="M12 10v1M12 17v1M8 14h1M15 14h1"/></svg></span></i>
    <span class="hl">Custom</span> GUI
  </div>
  <div class="feature" style="left:248px; top:228px;">
    <i class="feature-icon"><span><svg viewBox="0 0 24 24"><rect x="3" y="4" width="18" height="16" rx="1"/><path d="M3 8h18"/><circle cx="12" cy="14" r="3"/><path d="M12 9.5v1.5M12 17v1.5M7.5 14H9M15 14h1.5"/></svg></span></i>
    <span class="hl">HL7</span><br>Integration
  </div>

  <div class="feature" style="left:104px; top:301px;">
    <i class="feature-icon"><span><svg viewBox="0 0 24 24"><path d="M5 4h3l2 4-2 2a10 10 0 005 5l2-2 4 2v3a2 2 0 01-2 2A16 16 0 013 6a2 2 0 012-2z"/><circle cx="17" cy="7" r="4"/><path d="M17 5v4M15 7h4"/></svg></span></i>
    <span class="hl">Nurse call<br>handset</span><br>compatible
  </div>
  <div class="feature" style="left:202px; top:301px;">
    <i class="feature-icon"><span><svg viewBox="0 0 24 24"><circle cx="12" cy="12" r="9"/><path d="M3 12h18M12 3c3 3 3 15 0 18M12 3c-3 3-3 15 0 18"/></svg></span></i>
    <span class="hl">Web-based<br>compatible</span><br>content
  </div>

  <footer class="page-footer">
    <svg width="300" height="36" viewBox="0 0 300 36">
      <rect x="0" y="9" width="300" height="27" fill="var(--navy)"/>
      <polygon points="159,36 175,0 300,0 300,36" fill="var(--teal)"/>
    </svg>
    <span class="footer-url">www.wardlight.com</span>
    <span class="footer-brand footer-brand--light">NVQ</span>
  </footer>
</section>

<section class="page page--intro">
  <div class="intro-photo" role="img" aria-label="Photo of a female doctor with a stethoscope showing a clipboard to a young female patient"></div>
  <div class="page-frame"></div>
  <h2 class="headline">
    <span class="line-teal">Smart Patient</span>
    <span class="line-navy">Engagement Solution</span>
  </h2>
  <p class="intro-body"><b>NVQ</b> is a caring and consultative long-term hospital partner. The solutions delivered through our <b>Meridel</b> are empowering to healthcare workers, patients, their families and caregivers. In addition to giving the hospital an instant modern facelift.</p>
  <p class="intro-lead"><b>Meridel</b> supports the hospital to:</p>
  <p class="intro-tagline">ENTERTAIN, EDUCATE &amp; ENGAGE</p>
  <footer class="page-footer">
    <svg width="300" height="36" viewBox="0 0 300 36">
      <rect x="0" y="9" width="300" height="27" fill="var(--navy)"/>
      <polygon points="159,36 175,0 300,0 300,36" fill="var(--teal)"/>
    </svg>
    <span class="footer-url">www.wardlight.com</span>
    <span class="footer-brand footer-brand--light">NVQ</span>
  </footer>
</section>

</body>
</html>
```